Business Card Design for Engineering Firm

Need a business card design for small mechanical and plumbing engineering form based in Utah. Design should be customizable for all employees.

```html
<!DOCTYPE html>
<html lang="en">
<head>
<meta charset="utf-8">
<title>Kestrel Engineering – Business Card</title>
<link href="https://fonts.googleapis.com/css2?family=Montserrat:wght@400;600;700&display=swap" rel="stylesheet">
<style>
  :root {
    --bg: #2b2b2d;
    --brand-red: #8b1a14;
    --brand-red-dark: #5e100c;
    --brand-red-light: #a8332b;
    --steel: #555555;
    --text: #333333;
    --card-white: #ffffff;
  }
  * { margin: 0; padding: 0; box-sizing: border-box; }
  html, body {
    width: 1200px; height: 1186px; overflow: hidden;
    background: var(--bg);
    font-family: "Montserrat", sans-serif;
  }
  .stage { position: relative; width: 1200px; height: 1186px; }

  .card {
    position: absolute; left: 150px; width: 900px; height: 514px;
    border-radius: 28px; overflow: hidden;
  }
  .card-back { top: 50px; }
  .card-front { top: 622px; background: var(--card-white); }

  .back-pattern {
    position: absolute; inset: 0;
    background: radial-gradient(circle at 25% 60%, var(--brand-red-light) 0%, var(--brand-red) 45%, var(--brand-red-dark) 100%);
  }
  .back-name {
    position: absolute; right: 90px; top: 210px;
    color: #ffffff; font-weight: 700; font-size: 30px; letter-spacing: 2px;
  }

  .wordmark {
    position: absolute; left: 70px; top: 150px;
    color: var(--brand-red); font-weight: 700; font-size: 46px;
    letter-spacing: 1px; line-height: 1.1;
  }
  .mark-block {
    position: absolute; right: 90px; top: 110px;
    width: 240px; height: 240px; background: var(--brand-red);
  }
  .person { position: absolute; left: 70px; top: 300px; color: var(--text); }
  .person-name { color: var(--brand-red); font-weight: 700; font-size: 28px; }
  .person-role { font-size: 18px; margin-top: 2px; }
  .address { position: absolute; left: 70px; top: 378px; font-size: 17px; line-height: 1.3; color: var(--text); }
  .contacts {
    position: absolute; left: 430px; top: 370px; list-style: none;
    font-size: 17px; line-height: 1.45; color: var(--text);
  }
  .contacts li { display: flex; align-items: center; gap: 10px; }
  .contacts svg { width: 16px; height: 16px; fill: var(--brand-red); flex: none; }
</style>
</head>
<body>
<main class="stage">
  <section class="card card-back">
    <div class="back-pattern" role="img" aria-label="Red background with repeating embossed brand pattern"></div>
    <span class="back-name">KESTREL ENGINEERING</span>
  </section>

  <section class="card card-front">
    <h1 class="wordmark">KESTREL<br>ENGINEERING</h1>
    <div class="mark-block"></div>

    <div class="person">
      <p class="person-name">Daniel Harper</p>
      <p class="person-role">Owner</p>
    </div>
    <p class="address">Lindenweg 42<br>20095 Hamburg</p>

    <ul class="contacts">
      <li><svg viewBox="0 0 16 16"><path d="M3 1h3l1.5 4-2 1.3a9 9 0 0 0 4.2 4.2L11 8.5 15 10v3a2 2 0 0 1-2 2A12 12 0 0 1 1 3a2 2 0 0 1 2-2z"/></svg>+49 401 555 0182</li>
      <li><svg viewBox="0 0 16 16"><path d="M4 0h8a1 1 0 0 1 1 1v14a1 1 0 0 1-1 1H4a1 1 0 0 1-1-1V1a1 1 0 0 1 1-1zm1 2v10h6V2zm3 11a1 1 0 1 0 0 2 1 1 0 0 0 0-2z"/></svg>+49 401 555 0182</li>
      <li><svg viewBox="0 0 16 16"><path d="M0 3h16v10H0zm1.5 1.2V12h13V4.2L8 9z"/></svg>info@kestrel-eng.com</li>
      <li><svg viewBox="0 0 16 16"><circle cx="8" cy="8" r="7.5"/></svg>www.kestrel-eng.com</li>
    </ul>
  </section>
</main>
</body>
</html>
```